REDESIGN MAIN BANNER IMAGE FOR MARKETING WEBSITE

I feel like my main banner image is too busy but I like it but i want to see other options. www.brightlanepromoworks.biz I want a nice professional clean design that goes with current theme of site. Must look professional and show the variety of incentives we offer but not be overwelming.

My business is called Brightlane Promo Works and I provide businesses around the world with marketing incentives that they can use to create exciting promotions and contest and marketing giveaways to help attract more customers.

I provide a variety of different types of incentives such as Vacation Certificates, Dining Vouchers, Hotel Savings Cards, Smart Watches, Etc. that businesses can use in their marketing efforts.

I want my main banner image to reflect the variety of different categories of incentives... that I offer here: https://www.brightlanepromoworks.biz/incentives

We can use images of certificates or images.....I just want the content to be the same:

CONTENT FOR MAIN BANNER IMAGE:
INCREASE LEADS AND SALES OVERNIGHT

CREATE EXCITING MARKETING PROMOTIONS GIVING AWAY SMART DEVICES, VACATION CERTIFICATES, DINING VOUCHERS AND OTHER INCENTIVES TO YOUR CUSTOMERS

GET A FREE SAMPLE PACKAGE FOR A LIMITED TIME ONLY

Target Market(s)

b2b business owners, ceo, president, owner, founder

Industry/Entity Type

Promotional

Requirements
Must have
• Hi guys keep in mind the finished product will have to be 1800x840

Nice to have
• I want a nice professional clean design that goes with current theme of site. Must look professional and show the variety of incentives we offer but not be overwelming.
Should not have

```html
<!DOCTYPE html>
<html lang="en">
<head>
<meta charset="utf-8">
<title>Brightlane Promo Works – Main Banner</title>
<link href="https://fonts.googleapis.com/css2?family=Oswald:wght@400;500;600;700&family=Montserrat:wght@400;500;600;700;800&family=Exo+2:wght@400;700&display=swap" rel="stylesheet">
<style>
:root{
  --stage:#3b3b3b;
  --orange:#ff5a00;
  --navy:#0c1b3d;
  --yellow:#ffe14a;
  --red:#f2151f;
  --blue:#0b5aa3;
  --deep-blue:#0a4f95;
  --green:#4caf50;
  --lilac:#c8c4f2;
  --paper:#f4f4f4;
  --ink:#222;
  --card-red:#c4121a;
}
*{margin:0;padding:0;box-sizing:border-box}
html,body{width:1200px;height:764px;overflow:hidden;background:var(--stage)}
.page{position:absolute;left:0;top:96px;width:1200px;height:571px;overflow:hidden;background:#fff}

/* promo bar */
.promo-bar{position:absolute;left:0;top:0;width:1200px;height:69px;background:var(--orange);font-family:"Exo 2",sans-serif;color:#fff}
.promo-headline{position:absolute;left:183px;top:8px;font-size:28px;white-space:nowrap;line-height:38px}
.promo-headline strong{font-size:36px;font-weight:700}
.promo-input{position:absolute;left:611px;top:8px;width:230px;height:38px;background:#fff;color:#8a8a8a;font-size:15px;line-height:38px;padding-left:10px}
.promo-button{position:absolute;left:841px;top:8px;width:157px;height:38px;background:var(--navy);color:#fff;font-size:17px;line-height:38px;text-align:center}
.promo-close{position:absolute;left:1149px;top:25px;width:20px;height:20px;border-radius:50%;background:#fff}
.promo-note{position:absolute;left:632px;top:52px;font-family:Montserrat,sans-serif;font-weight:800;font-size:13px;color:var(--yellow);white-space:nowrap;letter-spacing:.2px}

/* hero */
.hero{position:absolute;left:0;top:69px;width:1200px;height:502px;background:linear-gradient(100deg,#f1f1f1 0%,#fafafa 55%,#fff 100%);overflow:hidden}
.hero-shapes{position:absolute;left:0;top:0}
.headline{position:absolute;left:68px;top:44px;font-family:Oswald,sans-serif;font-weight:700;color:var(--red);font-size:76px;line-height:73px;letter-spacing:.5px;transform:scaleX(1.02);transform-origin:left}
.subline{position:absolute;left:72px;top:194px;width:590px;font-family:Montserrat,sans-serif;font-weight:500;color:var(--deep-blue);font-size:17.4px;line-height:28.5px;letter-spacing:.2px}
.offer{position:absolute;left:70px;top:283px;font-family:Oswald,sans-serif;font-weight:600;color:var(--deep-blue);font-size:25px;white-space:nowrap}
.offer .free{color:var(--green);font-size:40px;font-weight:700}
.offer .limited{color:var(--red)}
.cta{position:absolute;left:153px;top:350px;width:396px;height:92px}
.cta svg{position:absolute;left:0;top:0}
.cta-title{position:absolute;left:0;width:396px;top:10px;text-align:center;font-family:Montserrat,sans-serif;font-weight:800;font-size:37px;color:#fff;letter-spacing:.5px}
.cta-sub{position:absolute;left:0;width:396px;top:50px;text-align:center;font-family:Montserrat,sans-serif;font-weight:400;font-size:25px;color:var(--lilac)}

/* incentive certificates */
.cards{position:absolute;left:0;top:0;width:1200px;height:502px;clip-path:polygon(842px 0,1200px 0,1200px 502px,668px 502px,842px 66px)}
.card{position:absolute;width:130px;background:#fff;border:1px solid #ddd;font-family:Oswald,sans-serif;overflow:hidden;display:flex;flex-direction:column}
.card-photo{height:52%;position:relative}
.card-title{position:absolute;left:5px;top:4px;color:#fff;font-size:13px;font-weight:500;line-height:14px;width:80px}
.card-title b{background:var(--red);font-size:8px;padding:0 2px;font-weight:600}
.card-logo{position:absolute;right:5px;top:4px;color:#fff;font-size:8px;font-weight:600;opacity:.85}
.card-band{background:var(--card-red);color:#fff;font-size:5px;font-weight:500;padding:2px 4px;letter-spacing:.2px}
.card-body{flex:1;padding:3px 4px;font-family:Montserrat,sans-serif;font-size:4.5px;color:#444;line-height:6px}
.card-body .label{color:var(--card-red);font-weight:700;display:block;margin-top:2px}
.card-foot{border-top:1px solid #ccc;padding:2px 4px;font-family:Montserrat,sans-serif;font-size:4.2px;color:var(--ink);line-height:5.5px;display:flex;justify-content:space-between}
.card-foot .url{color:var(--card-red);font-weight:700}
.tone-hotel{background:linear-gradient(160deg,#6d8aa6,#3d4c5a 60%,#8b6b52)}
.tone-cruise{background:linear-gradient(180deg,#6fa8dc,#2c6aa0 60%,#e9eef2)}
.tone-tech{background:linear-gradient(150deg,#4a6fa8,#2a2f44 55%,#b0875d)}
.tone-speaker{background:linear-gradient(160deg,#8aa0b8,#1d4f8c 55%,#d8c7a8)}
.tone-health{background:linear-gradient(160deg,#cfe6f2,#6aa3c8 60%,#f1f6fa)}
.tone-flight{background:linear-gradient(180deg,#9ec9ef,#4f8fc8 60%,#e8eef5)}
.tone-dining{background:linear-gradient(160deg,#7a3b2a,#3a1e18 55%,#c98a4e)}
.tone-lounge{background:linear-gradient(170deg,#5f7690,#2c3b4c 60%,#9aa8b6)}
</style>
</head>
<body>
<div class="page">

  <header class="promo-bar">
    <div class="promo-headline">Get <strong>65%</strong> OFF Your First Month</div>
    <div class="promo-input">Mobile Number</div>
    <div class="promo-button">Get My Discount</div>
    <div class="promo-close">
      <svg width="20" height="20" viewBox="0 0 20 20"><path d="M6.5 6.5l7 7M13.5 6.5l-7 7" stroke="var(--orange)" stroke-width="2" stroke-linecap="round"/></svg>
    </div>
    <div class="promo-note">NEW CUSTOMERS ONLY - LIMITED TIME ONLY!</div>
  </header>

  <section class="hero">
    <svg class="hero-shapes" width="1200" height="502" viewBox="0 0 1200 502">
      <polygon points="700,0 1200,0 1200,502 560,502" fill="#e9e9e9"/>
      <polygon points="880,0 1200,0 1200,502 700,502" fill="#f6f6f6"/>
      <polygon points="0,0 100,0 0,130" fill="var(--blue)"/>
      <polygon points="630,502 668,502 842,66 804,66" fill="var(--blue)"/>
      <polygon points="785,110 812,110 790,150 770,150" fill="var(--blue)"/>
    </svg>

    <h1 class="headline">INCREASE LEADS AND<br>SALES OVERNIGHT</h1>
    <p class="subline">CREATE EXCITING MARKETING PROMOTIONS GIVING AWAY SMART DEVICES, VACATION CERTIFICATES, DINING VOUCHERS AND OTHER INCENTIVES TO YOUR CUSTOMERS</p>
    <p class="offer">GET A <span class="free">FREE</span> SAMPLE PACKAGE FOR A <span class="limited">LIMITED TIME</span> ONLY</p>

    <div class="cta">
      <svg width="396" height="92" viewBox="0 0 396 92">
        <ellipse cx="198" cy="86" rx="180" ry="5" fill="#000" opacity=".12"/>
        <path d="M2 2 L396 0 L390 82 Q198 90 8 82 Z" fill="var(--green)"/>
      </svg>
      <div class="cta-title">GET FREE SAMPLE</div>
      <div class="cta-sub">100% FREE</div>
    </div>

    <div class="cards">
      <!-- row 1 -->
      <article class="card" style="left:815px;top:0;height:150px">
        <div class="card-photo tone-hotel" role="img" aria-label="Hotel pool and suite photos"><div class="card-title">Hotel Accommodations</div></div>
        <div class="card-band">EXCLUSIVELY FOR: CUSTOMER NAME</div>
        <div class="card-body">Redeem online for full offer details.<span class="label">FEATURES</span>Redeem online for full offer details.</div>
        <div class="card-foot"><span>#10983-95930</span><span class="url">WWW.PERKVAULTREWARDS.COM</span></div>
      </article>
      <article class="card" style="left:952px;top:0;height:150px">
        <div class="card-photo tone-hotel" role="img" aria-label="Hotel pool and suite photos"><div class="card-title">3 Star Hotel Stays</div></div>
        <div class="card-band">EXCLUSIVELY FOR: CUSTOMER NAME</div>
        <div class="card-body">Redeem online for full offer details.<span class="label">FEATURES</span>Redeem online for full offer details.</div>
        <div class="card-foot"><span>#10983-95930</span><span class="url">WWW.PERKVAULTREWARDS.COM</span></div>
      </article>
      <article class="card" style="left:1089px;top:0;height:150px;width:120px">
        <div class="card-photo tone-cruise" role="img" aria-label="Cruise ship and beach resort photos"><div class="card-title">4 Night Cruise Getaway</div></div>
        <div class="card-band">EXCLUSIVELY FOR: CUSTOMER NAME</div>
        <div class="card-body">Redeem online for full offer details.<span class="label">FEATURES</span>Redeem online for full offer details.</div>
        <div class="card-foot"><span>#10983-95930</span><span class="url">WWW.PERKVAULTREWARDS.COM</span></div>
      </article>

      <!-- row 2 -->
      <article class="card" style="left:680px;top:157px;height:172px">
        <div class="card-photo tone-tech" role="img" aria-label="Smart device product photos"><div class="card-title">ENJOY <b>SMART WATCH</b></div></div>
        <div class="card-band">EXCLUSIVELY FOR: CUSTOMER NAME</div>
        <div class="card-body">Redeem online for full offer details.<span class="label">FEATURES</span>Redeem online for full offer details.</div>
        <div class="card-foot"><span>#10983-95930</span><span class="url">WWW.PERKVAULTREWARDS.COM</span></div>
      </article>
      <article class="card" style="left:815px;top:157px;height:172px">
        <div class="card-photo tone-tech" role="img" aria-label="Music player and listener photos"><div class="card-title">ENJOY <b>MP4 PLAYER</b></div><div class="card-logo">LOGO</div></div>
        <div class="card-band">EXCLUSIVELY FOR: CUSTOMER NAME</div>
        <div class="card-body">Redeem online for full offer details.<span class="label">FEATURES</span>Redeem online for full offer details.</div>
        <div class="card-foot"><span>#10983-95930</span><span class="url">WWW.PERKVAULTREWARDS.COM</span></div>
      </article>
      <article class="card" style="left:952px;top:157px;height:172px">
        <div class="card-photo tone-speaker" role="img" aria-label="Portable speaker on a beach photo"><div class="card-title">ENJOY <b>SPEAKER</b></div><div class="card-logo">LOGO</div></div>
        <div class="card-band">EXCLUSIVELY FOR: CUSTOMER NAME</div>
        <div class="card-body">Redeem online for full offer details.<span class="label">FEATURES</span>Redeem online for full offer details.</div>
        <div class="card-foot"><span>#10983-95930</span><span class="url">WWW.PERKVAULTREWARDS.COM</span></div>
      </article>
      <article class="card" style="left:1089px;top:157px;height:172px;width:120px">
        <div class="card-photo tone-health" role="img" aria-label="Pharmacy and prescription photos"><div class="card-title">FREE <b>DISCOUNT CARD</b></div><div class="card-logo">LOGO</div></div>
        <div class="card-band">EXCLUSIVELY FOR: CUSTOMER NAME</div>
        <div class="card-body">Redeem online for full offer details.<span class="label">FEATURES</span>Redeem online for full offer details.</div>
        <div class="card-foot"><span>#10983-95930</span><span class="url">WWW.PERKVAULTREWARDS.COM</span></div>
      </article>

      <!-- row 3 -->
      <article class="card" style="left:680px;top:336px;height:172px">
        <div class="card-photo tone-flight" role="img" aria-label="Airplane and hotel photos"><div class="card-title">AIRFARE <b>HOTEL</b></div><div class="card-logo">LOGO</div></div>
        <div class="card-band">EXCLUSIVELY FOR: CUSTOMER NAME</div>
        <div class="card-body">Redeem online for full offer details.<span class="label">FEATURES</span>Redeem online for full offer details.</div>
        <div class="card-foot"><span>#10983-95930</span><span class="url">WWW.PERKVAULTREWARDS.COM</span></div>
      </article>
      <article class="card" style="left:815px;top:336px;height:172px">
        <div class="card-photo tone-dining" role="img" aria-label="Restaurant dining photos"><div class="card-title">ENJOY <b>$25 OFF</b></div><div class="card-logo">LOGO</div></div>
        <div class="card-band">EXCLUSIVELY FOR: CUSTOMER NAME</div>
        <div class="card-body">Redeem online for full offer details.<span class="label">FEATURES</span>Redeem online for full offer details.</div>
        <div class="card-foot"><span>#10983-95930</span><span class="url">WWW.PERKVAULTREWARDS.COM</span></div>
      </article>
      <article class="card" style="left:952px;top:336px;height:172px">
        <div class="card-photo tone-lounge" role="img" aria-label="Hotel lobby and travel photos"><div class="card-title">ENJOY <b>$100 OFF</b></div><div class="card-logo">LOGO</div></div>
        <div class="card-band">EXCLUSIVELY FOR: CUSTOMER NAME</div>
        <div class="card-body">Redeem online for full offer details.<span class="label">FEATURES</span>Redeem online for full offer details.</div>
        <div class="card-foot"><span>#10983-95930</span><span class="url">WWW.PERKVAULTREWARDS.COM</span></div>
      </article>
      <article class="card" style="left:1089px;top:336px;height:172px;width:120px">
        <div class="card-photo tone-lounge" role="img" aria-label="Hotel lobby and travel photos"><div class="card-title">ENJOY <b>$400 OFF</b></div><div class="card-logo">LOGO</div></div>
        <div class="card-band">EXCLUSIVELY FOR: CUSTOMER NAME</div>
        <div class="card-body">Redeem online for full offer details.<span class="label">FEATURES</span>Redeem online for full offer details.</div>
        <div class="card-foot"><span>#10983-95930</span><span class="url">WWW.PERKVAULTREWARDS.COM</span></div>
      </article>
    </div>
  </section>
</div>
</body>
</html>
```